A clean modern user interface design for a smart home control system

Design Brief: Smart Home Interface Development
Project Overview
We are initiating a new project to develop a sophisticated smart home interface. This interface will be the central hub for controlling and managing various aspects of a smart home, including CCTV, Smart TV, Quorvel TV, home cinema using Vantromere, lighting, shades, HVAC, and audio systems. With no pre-existing designs or frameworks, this project offers a unique opportunity to create a fresh and innovative interface from the ground up. We aim to take inspiration from Quorvel’s renowned UI/UX design style, which is celebrated for its elegance, simplicity, and intuitive user experience. Additionally, the design should include the ability to switch between ‘light’ and ‘dark’ modes, reflecting modern user preferences for customizable visual themes.
Objectives
•	Innovation: Create a cutting-edge interface that sets a new standard for smart home control systems, drawing inspiration from Quorvel’s clean, minimalistic, and user-friendly approach.
•	User-Centric Design: Develop an intuitive interface that caters to a broad range of users, ensuring that both tech-savvy individuals and those less familiar with smart technology can navigate it with ease.
•	Consistency: Establish a cohesive design language across the interface, maintaining uniformity in style, typography, and colour palette, while reflecting the sophistication and simplicity of Quorvel’s design ethos.
•	Light and Dark Modes: Design the interface with the capability to switch between light and dark modes, allowing users to choose their preferred visual style for different environments and personal preferences.
•	Responsiveness: Create a fully responsive interface in both Landsthat functions seamlessly across various screen sizes and devices, including tablets, smartphones, and in-wall panels.
•	Integration: Seamlessly incorporate controls for CCTV, Smart TV, Quorvel TV, lighting, shades, HVAC, and audio into a single, unified interface that allows users to manage all aspects of their smart home effortlessly.
Target Audience
The primary users of this interface are homeowners who desire a luxurious and intuitive smart home experience. The design should appeal to both advanced users who require comprehensive functionality and those who prioritize simplicity and elegance. Additionally, the interface should be straightforward for integrators who configure and maintain these systems.
Design Elements
1.	Overall Aesthetic
•	Style: Emulate Quorvel’s clean, minimalist, and modern aesthetic that conveys high-end luxury and sophistication.
•	Typography: Select modern, legible fonts that enhance readability, reflecting Quorvel’s preference for clear and elegant typefaces. Sans-serif fonts, similar to Quorvel’s system fonts like San Francisco, are recommended.
•	Colour Palette: Design a neutral colour palette with subtle, refined accents. Include both light and dark mode options, allowing users to choose between a brighter, more energetic theme and a darker, more subdued theme that is easier on the eyes in low-light environments.
•	Icons: Design custom, vector-based icons that are sleek, intuitive, and consistent, taking inspiration from Quorvel’s iconic design language.
2.	User Interface Components
•	Navigation: Implement a simplified, intuitive navigation system that allows users to easily access different control sections (e.g., lighting, audio, CCTV), similar to the seamless navigation found in Quorvel’s uXa and teluX interfaces.
•	Dashboard: Create a home dashboard that provides a clear overview of key system statuses and quick access to frequently used controls, with a design inspired by the clarity and organisation of Quorvel’s Pivot Deck. Ensure that the dashboard looks equally effective in both light and dark modes.
•	Control Pages:
•	CCTV: Design live camera feed pages with options for full-screen viewing, recording controls, and playback functionality, focusing on a clean and user-friendly layout that adapts well to both light and dark modes.
•	Smart TV/Quorvel TV: Develop control panels for power, volume, channel/menu navigation, and input switching, reflecting Quorvel’s approach to simplicity and ease of use, with clear visibility in both visual modes.
•	Lighting & Shades: Incorporate intuitive sliders or toggles for controlling individual or grouped lights and shades, with options for scene creation and activation, designed for seamless use in light and dark modes.
•	HVAC: Design user-friendly temperature controls, including settings for scheduling, mode selection, and real-time adjustments, inspired by Quorvel’s seamless integration of function and form. Ensure readability and ease of use in both visual themes.
•	Audio: Develop multi-room audio controls that allow users to select sources, adjust volume, and manage audio zones easily, taking cues from Quorvel’s focus on intuitive and enjoyable user experiences, with consistent performance across both light and dark modes.
3.	User Experience
•	Flow: Ensure a logical user journey with smooth transitions between different controls, mimicking Quorvel’s emphasis on seamless and intuitive navigation.
•	Feedback: Provide immediate and clear feedback for user actions, such as toggling a light or changing a temperature setting, inspired by the responsive and satisfying interactions found in Quorvel’s designs.
•	Accessibility: Incorporate accessibility features, such as adjustable text sizes and potential voice control integration, in line with Quorvel’s commitment to inclusivity and user accessibility.
4.	Technical Requirements
•	Photoshop Design: All designs should be created in Adobe Photoshop (.psd) with organized groups and layers. Interface elements must be grouped logically, allowing for quick export and bulk saving. Ensure that each component (buttons, icons, sliders, etc.) is easily identifiable and can be individually exported for development purposes. Include separate groups for light and dark mode elements to ensure consistency across themes.
•	Responsive Design: Ensure the designs are adaptable for different screen sizes and orientations, including tablets, smartphones, and in-wall panels.
•	Performance: Design elements should be optimized for quick loading and smooth operation, even when managing multiple devices simultaneously.
Success Criteria
•	A user interface that is well-received for its modern design, ease of use, and clear inspiration from Quorvel’s iconic design style.
•	A fully responsive design that performs seamlessly across all intended devices.
•	Positive feedback from users and integrators, with strong engagement metrics, particularly in how well the light and dark modes are received.
Additional Notes
We look forward to seeing a design that not only meets our objectives but also reflects the elegance, usability, and flexibility that Quorvel’s design style is renowned for, offering a seamless experience in both light and dark modes.

High end residential end user

```html
<!DOCTYPE html>
<html lang="en">
<head>
<meta charset="utf-8">
<title>Smart Home Control Panel — Dark and Light Modes</title>
<link rel="stylesheet" href="https://fonts.googleapis.com/css2?family=Roboto:wght@400;500;700&display=swap">
<style>
  :root {
    --accent: #f2742b;
    --page-bg: #e6e6e6;
    --dial-top: #4a4a4a;
    --dial-bottom: #0e0e0e;
  }
  html, body {
    margin: 0; padding: 0;
    width: 784px; height: 1200px;
    overflow: hidden;
    background: var(--page-bg);
    font-family: "Roboto", Arial, sans-serif;
  }
  .frame {
    position: absolute; left: 32px;
    width: 720px; height: 540px;
    overflow: hidden;
    border-radius: 4px;
  }
  .frame--dark { top: 30px; }
  .frame--light { top: 630px; }

  .screen {
    position: absolute; left: 0; top: 0;
    width: 1367px; height: 1024px;
    transform: scale(0.5267);
    transform-origin: 0 0;
    background: var(--bg);
    color: var(--text);
  }
  .theme-dark {
    --bg: #151515;
    --card: #262626;
    --text: #ffffff;
    --muted: #8c8c8c;
    --faint: #6a6a6a;
    --cloud-front: #ffffff;
    --cloud-stroke: #ffffff;
    --cloud-back: #8d8d8d;
    --track: #4a4a4a;
    --track-fill: #9a9a9a;
    --mode-btn: #5c5c5c;
    --pill: #5a5a5a;
    --home: #9a9a9a;
    --temp: #8e8e8e;
    --toggle-bg: #7a7a7a;
    --toggle-knob: #2a2a2a;
  }
  .theme-light {
    --bg: #f3f3f1;
    --card: #e2e2e2;
    --text: #1e1e1e;
    --muted: #6f6f6f;
    --faint: #9a9a9a;
    --cloud-front: #ffffff;
    --cloud-stroke: #7a7a7a;
    --cloud-back: #8d8d8d;
    --track: #b0b0b0;
    --track-fill: #555555;
    --mode-btn: #5c5c5c;
    --pill: #5f5f5f;
    --home: #555555;
    --temp: #5a5a5a;
    --toggle-bg: #5a5a5a;
    --toggle-knob: #ffffff;
  }

  .abs { position: absolute; }

  /* top bar */
  .home-icon { left: 38px; top: 52px; width: 38px; height: 40px; }
  .clock { left: 105px; top: 52px; font-size: 33px; color: var(--muted); font-weight: 500; }
  .nav { left: 792px; top: 58px; display: flex; gap: 32px; font-size: 24px; }
  .nav a { color: var(--muted); text-decoration: none; }
  .nav a.is-active { color: var(--text); }
  .status-icons { left: 1266px; top: 10px; width: 58px; height: 22px; }
  .avatar {
    left: 1264px; top: 47px; width: 70px; height: 70px; border-radius: 50%;
    background: radial-gradient(circle at 50% 55%, #f6f1f2 0 35%, #e9b8c4 60%, #c98393 100%);
  }

  /* weather */
  .cloud { left: 38px; top: 183px; width: 210px; height: 116px; }
  .temperature { left: 158px; top: 318px; font-size: 48px; font-weight: 700; color: var(--temp); }
  .condition { left: 160px; top: 366px; font-size: 20px; color: var(--muted); }

  /* cards */
  .card { background: var(--card); border-radius: 12px; }
  .card-title { position: absolute; font-size: 20px; font-weight: 500; color: var(--text); }
  .power { position: absolute; width: 26px; height: 26px; }

  /* picker */
  .picker {
    position: absolute; width: 180px;
    display: flex; flex-direction: column; align-items: center;
    color: var(--muted);
  }
  .picker svg { width: 14px; height: 10px; }
  .picker .pk-side { font-size: 15px; line-height: 22px; color: var(--muted); }
  .picker .pk-cur { font-size: 20px; line-height: 36px; color: var(--text); }

  /* lighting */
  .color-wheel {
    left: 366px; top: 222px; width: 150px; height: 150px; border-radius: 50%;
    background:
      radial-gradient(circle, rgba(255,255,255,0.95) 0%, rgba(255,255,255,0) 70%),
      conic-gradient(#ff3b3b, #ff9d2b, #ffe93a, #6cf04f, #31e0d0, #3a7bff, #8a3bff, #ff3bd8, #ff3b3b);
  }
  .brightness { left: 345px; top: 381px; width: 200px; height: 18px; }

  /* hvac */
  .dial {
    left: 1129px; top: 440px; width: 176px; height: 176px; border-radius: 50%;
    background: radial-gradient(circle at 50% 20%, var(--dial-top), var(--dial-bottom) 75%);
    box-shadow: 0 0 0 3px rgba(140,140,140,0.35), 0 8px 18px rgba(0,0,0,0.35);
    display: flex; flex-direction: column; align-items: center; justify-content: center;
    color: #fff;
  }
  .dial-value { font-size: 48px; font-weight: 500; line-height: 50px; }
  .dial-mode { font-size: 15px; }
  .mode-btn {
    position: absolute; top: 745px; width: 70px; height: 70px; border-radius: 10px;
    background: var(--mode-btn); color: #fff;
    display: flex; flex-direction: column; align-items: center; justify-content: center;
    font-size: 12px; gap: 4px;
  }
  .mode-btn svg { width: 34px; height: 34px; }
  .mode-btn.is-active { background: var(--accent); }
  .humidity {
    left: 1150px; top: 846px; width: 139px; height: 70px; border-radius: 10px;
    background: var(--pill); color: #fff;
    display: flex; align-items: center; justify-content: center; gap: 20px;
    font-size: 32px; font-weight: 500;
  }
  .humidity small { font-size: 13px; }

  /* audio */
  .album {
    left: 55px; top: 493px; width: 200px; height: 200px; border-radius: 10px;
    border: 2px solid #8a8a8a; box-sizing: border-box; overflow: hidden;
    background: radial-gradient(circle at 55% 40%, #b23bd6 0%, #5a1a86 55%, #22102f 100%);
  }
  .album-meta { position: absolute; left: 0; right: 0; top: 126px; text-align: center; color: #fff; }
  .album-meta .title { font-size: 15px; line-height: 15px; }
  .album-meta .artist { font-size: 11px; line-height: 12px; }
  .album-progress { position: absolute; left: 12px; right: 12px; top: 160px; height: 1px; background: #fff; }
  .album-controls { position: absolute; left: 20px; top: 166px; width: 160px; height: 26px; }
  .volume-knob {
    left: 105px; top: 709px; width: 100px; height: 100px; border-radius: 50%;
    border: 2px solid #9a9a9a; box-sizing: border-box;
    display: flex; align-items: center; justify-content: center;
  }
  .volume-knob .inner {
    width: 84px; height: 84px; border-radius: 50%;
    background: radial-gradient(circle at 50% 30%, #d8d8d8, #6e6e6e 80%);
    display: flex; flex-direction: column; align-items: center; justify-content: center;
    color: #fff; font-size: 28px; font-weight: 500; line-height: 28px;
  }
  .volume-knob .inner small { font-size: 11px; }
  .eq { left: 58px; top: 818px; width: 90px; height: 118px; }

  /* cctv */
  .cam {
    position: absolute; left: 322px; width: 200px; height: 200px; border-radius: 10px;
    border: 2px solid #9a9a9a; box-sizing: border-box; overflow: hidden;
    background: linear-gradient(180deg, #a9c7e6 0%, #cfd9d8 35%, #a46b52 55%, #b9aca4 80%, #8a8682 100%);
  }
  .cam-label { position: absolute; left: 8px; top: 8px; font-size: 15px; color: #fff; }
  .cam-bar { position: absolute; left: 0; right: 0; bottom: 0; height: 30px; background: rgba(40,40,40,0.55); }

  /* smart tv */
  .tv-screen {
    left: 591px; top: 493px; width: 385px; height: 297px; border-radius: 10px;
    border: 2px solid #9a9a9a; box-sizing: border-box; overflow: hidden; background: #111;
  }
  .tv-hero-a { position: absolute; left: 0; top: 0; width: 190px; height: 120px; background: linear-gradient(135deg, #f4b27c, #e77a3a 60%, #c85a24); }
  .tv-hero-b { position: absolute; left: 196px; top: 0; width: 187px; height: 120px; background: linear-gradient(180deg, #2f5560, #6e9ea3 50%, #1f3e4c); }
  .tv-row { position: absolute; left: 0; top: 146px; display: flex; gap: 4px; }
  .tv-row span { display: block; height: 84px; }
  .tv-apps { position: absolute; left: 0; top: 256px; display: flex; gap: 4px; }
  .tv-apps span { display: block; width: 34px; height: 34px; border-radius: 3px; background: #2b2b2b; }
  .tv-volume { left: 1016px; top: 493px; width: 20px; height: 297px; }
  .app-btn {
    position: absolute; width: 100px; height: 50px; border-radius: 10px; background: #111;
    color: #fff; display: flex; align-items: center; justify-content: center;
    font-size: 17px; font-weight: 500;
  }

  /* footer */
  .date { left: 43px; top: 966px; font-size: 22px; color: var(--muted); font-weight: 500; }
  .mode-toggle { left: 1283px; top: 971px; width: 66px; height: 22px; }
</style>
</head>
<body>

<!-- DARK MODE -->
<div class="frame frame--dark">
<div class="screen theme-dark">
  <svg class="abs home-icon" viewBox="0 0 38 40"><path d="M19 2 L36 16 V38 H25 V26 H13 V38 H2 V16 Z" fill="var(--home)"/></svg>
  <div class="abs clock">05:28</div>
  <nav class="abs nav"><a href="#">Home</a><a href="#" class="is-active">Control Panel</a><a href="#">Settings</a></nav>
  <svg class="abs status-icons" viewBox="0 0 58 22"><path d="M4 6 L14 15 L9 20 V2 L14 7 L4 16" fill="none" stroke="var(--text)" stroke-width="1.8"/><path d="M34 9 a14 14 0 0 1 20 0 M37 13 a9 9 0 0 1 14 0 M40 17 a4 4 0 0 1 8 0" fill="none" stroke="var(--text)" stroke-width="2.2" stroke-linecap="round"/><circle cx="44" cy="20" r="1.6" fill="var(--text)"/></svg>
  <div class="abs avatar" role="img" aria-label="User avatar"></div>

  <svg class="abs cloud" viewBox="0 0 210 116"><path d="M110 70 a28 28 0 0 1 22-40 a34 34 0 0 1 60 12 a22 22 0 0 1 8 42 H120 Z" fill="var(--cloud-back)"/><path d="M24 112 a22 22 0 0 1-4-44 a30 30 0 0 1 42-26 a40 40 0 0 1 74 18 a26 26 0 0 1 6 52 Z" fill="var(--cloud-front)" stroke="var(--cloud-stroke)" stroke-width="3"/></svg>
  <div class="abs temperature">26°F</div>
  <div class="abs condition">Cloudy</div>

  <!-- Lighting -->
  <section class="abs card" style="left:297px;top:163px;width:515px;height:250px"></section>
  <div class="card-title" style="left:314px;top:183px">Lighting &amp; Shades</div>
  <svg class="power" style="left:771px;top:177px" viewBox="0 0 26 26"><circle cx="13" cy="13" r="13" fill="var(--accent)"/><path d="M8.5 9 a6.5 6.5 0 1 0 9 0 M13 6 V13" fill="none" stroke="#fff" stroke-width="2" stroke-linecap="round"/></svg>
  <div class="abs color-wheel"></div>
  <svg class="abs brightness" viewBox="0 0 200 18"><circle cx="5" cy="9" r="4" fill="var(--track-fill)"/><rect x="15" y="5" width="166" height="8" rx="4" fill="none" stroke="var(--track)" stroke-width="1.5"/><rect x="15" y="5" width="112" height="8" rx="4" fill="var(--track-fill)"/><circle cx="192" cy="9" r="3" fill="var(--muted)"/><path d="M192 2V4M192 14V16M185 9H187M197 9H199M187 4L188.5 5.5M197 14L195.5 12.5M187 14L188.5 12.5M197 4L195.5 5.5" stroke="var(--muted)" stroke-width="1.2"/></svg>
  <div class="picker" style="left:600px;top:236px"><svg viewBox="0 0 14 10"><path d="M2 8 L7 3 L12 8" fill="none" stroke="currentColor" stroke-width="1.6"/></svg><span class="pk-side">Bedroom</span><span class="pk-cur">Living Room</span><span class="pk-side">Guest Room</span><svg viewBox="0 0 14 10"><path d="M2 2 L7 7 L12 2" fill="none" stroke="currentColor" stroke-width="1.6"/></svg></div>

  <section class="abs card" style="left:827px;top:163px;width:250px;height:250px"></section>
  <svg class="power" style="left:1038px;top:182px" viewBox="0 0 26 26"><circle cx="13" cy="13" r="13" fill="#8a8a8a"/><path d="M8.5 9 a6.5 6.5 0 1 0 9 0 M13 6 V13" fill="none" stroke="var(--card)" stroke-width="2" stroke-linecap="round"/></svg>

  <!-- HVAC -->
  <section class="abs card" style="left:1092px;top:163px;width:250px;height:780px"></section>
  <div class="card-title" style="left:1108px;top:184px">HVAC</div>
  <svg class="power" style="left:1300px;top:182px" viewBox="0 0 26 26"><circle cx="13" cy="13" r="13" fill="var(--accent)"/><path d="M8.5 9 a6.5 6.5 0 1 0 9 0 M13 6 V13" fill="none" stroke="#fff" stroke-width="2" stroke-linecap="round"/></svg>
  <div class="picker" style="left:1127px;top:243px"><svg viewBox="0 0 14 10"><path d="M2 8 L7 3 L12 8" fill="none" stroke="currentColor" stroke-width="1.6"/></svg><span class="pk-side">Bedroom</span><span class="pk-cur">Living Room</span><span class="pk-side">Guest Room</span><svg viewBox="0 0 14 10"><path d="M2 2 L7 7 L12 2" fill="none" stroke="currentColor" stroke-width="1.6"/></svg></div>
  <div class="abs dial"><span class="dial-value">20°C</span><span class="dial-mode">Cooling</span></div>
  <div class="mode-btn is-active" style="left:1102px"><svg viewBox="0 0 34 34"><path d="M17 3V31M5 10L29 24M5 24L29 10M13 5L17 9L21 5M13 29L17 25L21 29" fill="none" stroke="#fff" stroke-width="2.4" stroke-linecap="round"/></svg>Cooling</div>
  <div class="mode-btn" style="left:1181px"><svg viewBox="0 0 34 34"><path d="M10 5a4 4 0 0 1 8 0V20a7 7 0 1 1-8 0Z" fill="none" stroke="#fff" stroke-width="2.4"/><circle cx="14" cy="25" r="3.5" fill="#fff"/><path d="M22 8H30M22 13H28" stroke="#fff" stroke-width="2.4" stroke-linecap="round"/></svg>Heating</div>
  <div class="mode-btn" style="left:1260px"><svg viewBox="0 0 34 34"><path d="M4 12H22a4 4 0 1 0-4-4M4 18H28a4 4 0 1 1-4 4M4 24H16" fill="none" stroke="#fff" stroke-width="2.4" stroke-linecap="round"/></svg>Airwave</div>
  <div class="abs humidity"><svg width="10" height="12" viewBox="0 0 10 12"><path d="M5 1 C3 4 1 6 1 8 a4 4 0 0 0 8 0 C9 6 7 4 5 1Z" fill="#fff"/></svg><span>25<small>%</small></span></div>

  <!-- Audio -->
  <section class="abs card" style="left:32px;top:428px;width:250px;height:515px"></section>
  <div class="card-title" style="left:47px;top:445px">Audio</div>
  <svg class="power" style="left:243px;top:442px" viewBox="0 0 26 26"><circle cx="13" cy="13" r="13" fill="var(--accent)"/><path d="M8.5 9 a6.5 6.5 0 1 0 9 0 M13 6 V13" fill="none" stroke="#fff" stroke-width="2" stroke-linecap="round"/></svg>
  <div class="abs album" role="img" aria-label="Album artwork, glowing purple wall">
    <div class="album-meta"><div class="title">Music Title</div><div class="artist">Artist name</div></div>
    <div class="album-progress"></div>
    <svg class="album-controls" viewBox="0 0 160 26"><path d="M22 5V21M36 5L24 13L36 21Z" fill="#fff" stroke="#fff" stroke-width="2"/><circle cx="80" cy="13" r="12" fill="#fff"/><path d="M76 7L87 13L76 19Z" fill="#3a1650"/><path d="M124 5L136 13L124 21ZM138 5V21" fill="#fff" stroke="#fff" stroke-width="2"/></svg>
  </div>
  <div class="abs volume-knob"><div class="inner">50<small>%</small></div></div>
  <svg class="abs eq" viewBox="0 0 90 118"><g fill="none" stroke="var(--track)" stroke-width="7" stroke-linecap="round"><path d="M10 4V94M40 4V94M67 4V94"/></g><g fill="none" stroke="var(--track-fill)" stroke-width="7" stroke-linecap="round"><path d="M10 44V94M40 64V94M67 52V94"/></g><g fill="var(--track-fill)"><rect x="2" y="40" width="16" height="6" rx="2"/><rect x="32" y="60" width="16" height="6" rx="2"/><rect x="59" y="48" width="16" height="6" rx="2"/></g><g font-size="12" fill="var(--muted)" font-family="Roboto, sans-serif" text-anchor="middle"><text x="10" y="114">High</text><text x="40" y="114">Mid</text><text x="69" y="114">Low</text></g></svg>
  <div class="picker" style="left:122px;top:821px"><svg viewBox="0 0 14 10"><path d="M2 8 L7 3 L12 8" fill="none" stroke="currentColor" stroke-width="1.6"/></svg><span class="pk-side">Live</span><span class="pk-cur">Metal Rock</span><span class="pk-side">Rock</span><svg viewBox="0 0 14 10"><path d="M2 2 L7 7 L12 2" fill="none" stroke="currentColor" stroke-width="1.6"/></svg></div>

  <!-- CCTV -->
  <section class="abs card" style="left:297px;top:428px;width:250px;height:515px"></section>
  <div class="card-title" style="left:309px;top:443px">CCTV</div>
  <svg class="power" style="left:510px;top:440px" viewBox="0 0 26 26"><circle cx="13" cy="13" r="13" fill="var(--accent)"/><path d="M8.5 9 a6.5 6.5 0 1 0 9 0 M13 6 V13" fill="none" stroke="#fff" stroke-width="2" stroke-linecap="round"/></svg>
  <div class="cam" style="top:493px" role="img" aria-label="Camera 1 live feed, street with brick houses"><span class="cam-label">CAM 1</span><div class="cam-bar"><svg width="200" height="30" viewBox="0 0 200 30"><path d="M54 9L45 15L54 21ZM45 9L36 15L45 21Z" fill="#fff"/><circle cx="100" cy="15" r="9" fill="#fff"/><path d="M97 10L105 15L97 20Z" fill="#555"/><path d="M146 9L155 15L146 21ZM155 9L164 15L155 21Z" fill="#fff"/></svg></div></div>
  <div class="cam" style="top:721px" role="img" aria-label="Camera 2 live feed, street with brick houses"><span class="cam-label">CAM 2</span><div class="cam-bar"><svg width="200" height="30" viewBox="0 0 200 30"><path d="M54 9L45 15L54 21ZM45 9L36 15L45 21Z" fill="#fff"/><circle cx="100" cy="15" r="9" fill="#fff"/><path d="M97 10L105 15L97 20Z" fill="#555"/><path d="M146 9L155 15L146 21ZM155 9L164 15L155 21Z" fill="#fff"/></svg></div></div>

  <!-- Smart TV -->
  <section class="abs card" style="left:562px;top:428px;width:515px;height:515px"></section>
  <div class="card-title" style="left:580px;top:444px">Smart TV</div>
  <svg class="power" style="left:1038px;top:442px" viewBox="0 0 26 26"><circle cx="13" cy="13" r="13" fill="var(--accent)"/><path d="M8.5 9 a6.5 6.5 0 1 0 9 0 M13 6 V13" fill="none" stroke="#fff" stroke-width="2" stroke-linecap="round"/></svg>
  <div class="abs tv-screen" role="img" aria-label="TV home screen with featured shows, top picks and app list">
    <div class="tv-hero-a"></div><div class="tv-hero-b"></div>
    <div class="tv-row"><span style="width:104px;background:linear-gradient(180deg,#f3a33c,#b9451c)"></span><span style="width:46px;background:linear-gradient(180deg,#d9d3c7,#8a9a8f)"></span><span style="width:100px;background:linear-gradient(180deg,#9fc3d8,#e3ecf0)"></span><span style="width:48px;background:linear-gradient(180deg,#3b2f8c,#7b5bd0)"></span><span style="width:66px;background:linear-gradient(180deg,#d7d2ee,#8b7fc7)"></span></div>
    <div class="tv-apps"><span></span><span></span><span></span><span></span><span></span><span></span><span></span><span></span><span></span><span></span></div>
  </div>
  <svg class="abs tv-volume" viewBox="0 0 20 297"><rect x="1" y="1" width="18" height="295" rx="9" fill="none" stroke="var(--track)" stroke-width="1.5"/><rect x="1" y="120" width="18" height="176" rx="9" fill="var(--track-fill)"/><circle cx="10" cy="120" r="7" fill="#ddd"/></svg>
  <div class="app-btn" style="left:593px;top:808px">Flixora</div>
  <div class="app-btn" style="left:708px;top:808px">Streamly</div>
  <div class="app-btn" style="left:820px;top:808px">Dreamvale+</div>
  <div class="app-btn" style="left:710px;top:876px;font-size:15px">Nimbus Video</div>
  <div class="picker" style="left:912px;top:815px"><svg viewBox="0 0 14 10"><path d="M2 8 L7 3 L12 8" fill="none" stroke="currentColor" stroke-width="1.6"/></svg><span class="pk-side">Bedroom</span><span class="pk-cur">Living Room</span><span class="pk-side">Guest Room</span><svg viewBox="0 0 14 10"><path d="M2 2 L7 7 L12 2" fill="none" stroke="currentColor" stroke-width="1.6"/></svg></div>

  <div class="abs date">05/09/2024, Friday</div>
  <svg class="abs mode-toggle" viewBox="0 0 66 22"><rect x="1" y="1" width="64" height="20" rx="10" fill="var(--toggle-bg)"/><circle cx="52" cy="11" r="9" fill="var(--toggle-knob)"/></svg>
</div>
</div>

<!-- LIGHT MODE -->
<div class="frame frame--light">
<div class="screen theme-light">
  <svg class="abs home-icon" viewBox="0 0 38 40"><path d="M19 2 L36 16 V38 H25 V26 H13 V38 H2 V16 Z" fill="var(--home)"/></svg>
  <div class="abs clock">05:28</div>
  <nav class="abs nav"><a href="#">Home</a><a href="#" class="is-active">Control Panel</a><a href="#">Settings</a></nav>
  <svg class="abs status-icons" viewBox="0 0 58 22"><path d="M4 6 L14 15 L9 20 V2 L14 7 L4 16" fill="none" stroke="var(--text)" stroke-width="1.8"/><path d="M34 9 a14 14 0 0 1 20 0 M37 13 a9 9 0 0 1 14 0 M40 17 a4 4 0 0 1 8 0" fill="none" stroke="var(--text)" stroke-width="2.2" stroke-linecap="round"/><circle cx="44" cy="20" r="1.6" fill="var(--text)"/></svg>
  <div class="abs avatar" role="img" aria-label="User avatar"></div>

  <svg class="abs cloud" viewBox="0 0 210 116"><path d="M110 70 a28 28 0 0 1 22-40 a34 34 0 0 1 60 12 a22 22 0 0 1 8 42 H120 Z" fill="var(--cloud-back)"/><path d="M24 112 a22 22 0 0 1-4-44 a30 30 0 0 1 42-26 a40 40 0 0 1 74 18 a26 26 0 0 1 6 52 Z" fill="var(--cloud-front)" stroke="var(--cloud-stroke)" stroke-width="3"/></svg>
  <div class="abs temperature">26°F</div>
  <div class="abs condition">Cloudy</div>

  <section class="abs card" style="left:297px;top:163px;width:515px;height:250px"></section>
  <div class="card-title" style="left:314px;top:183px">Lighting &amp; Shades</div>
  <svg class="power" style="left:771px;top:177px" viewBox="0 0 26 26"><circle cx="13" cy="13" r="13" fill="var(--accent)"/><path d="M8.5 9 a6.5 6.5 0 1 0 9 0 M13 6 V13" fill="none" stroke="#fff" stroke-width="2" stroke-linecap="round"/></svg>
  <div class="abs color-wheel"></div>
  <svg class="abs brightness" viewBox="0 0 200 18"><circle cx="5" cy="9" r="4" fill="var(--track-fill)"/><rect x="15" y="5" width="166" height="8" rx="4" fill="none" stroke="var(--track)" stroke-width="1.5"/><rect x="15" y="5" width="112" height="8" rx="4" fill="var(--track-fill)"/><circle cx="192" cy="9" r="3" fill="var(--muted)"/><path d="M192 2V4M192 14V16M185 9H187M197 9H199M187 4L188.5 5.5M197 14L195.5 12.5M187 14L188.5 12.5M197 4L195.5 5.5" stroke="var(--muted)" stroke-width="1.2"/></svg>
  <div class="picker" style="left:600px;top:236px"><svg viewBox="0 0 14 10"><path d="M2 8 L7 3 L12 8" fill="none" stroke="currentColor" stroke-width="1.6"/></svg><span class="pk-side">Bedroom</span><span class="pk-cur">Living Room</span><span class="pk-side">Guest Room</span><svg viewBox="0 0 14 10"><path d="M2 2 L7 7 L12 2" fill="none" stroke="currentColor" stroke-width="1.6"/></svg></div>

  <section class="abs card" style="left:827px;top:163px;width:250px;height:250px"></section>
  <svg class="power" style="left:1038px;top:182px" viewBox="0 0 26 26"><circle cx="13" cy="13" r="13" fill="#6a6a6a"/><path d="M8.5 9 a6.5 6.5 0 1 0 9 0 M13 6 V13" fill="none" stroke="var(--card)" stroke-width="2" stroke-linecap="round"/></svg>

  <section class="abs card" style="left:1092px;top:163px;width:250px;height:780px"></section>
  <div class="card-title" style="left:1108px;top:184px">HVAC</div>
  <svg class="power" style="left:1300px;top:182px" viewBox="0 0 26 26"><circle cx="13" cy="13" r="13" fill="var(--accent)"/><path d="M8.5 9 a6.5 6.5 0 1 0 9 0 M13 6 V13" fill="none" stroke="#fff" stroke-width="2" stroke-linecap="round"/></svg>
  <div class="picker" style="left:1127px;top:243px"><svg viewBox="0 0 14 10"><path d="M2 8 L7 3 L12 8" fill="none" stroke="currentColor" stroke-width="1.6"/></svg><span class="pk-side">Bedroom</span><span class="pk-cur">Living Room</span><span class="pk-side">Guest Room</span><svg viewBox="0 0 14 10"><path d="M2 2 L7 7 L12 2" fill="none" stroke="currentColor" stroke-width="1.6"/></svg></div>
  <div class="abs dial"><span class="dial-value">20°C</span><span class="dial-mode">Cooling</span></div>
  <div class="mode-btn is-active" style="left:1102px"><svg viewBox="0 0 34 34"><path d="M17 3V31M5 10L29 24M5 24L29 10M13 5L17 9L21 5M13 29L17 25L21 29" fill="none" stroke="#fff" stroke-width="2.4" stroke-linecap="round"/></svg>Cooling</div>
  <div class="mode-btn" style="left:1181px"><svg viewBox="0 0 34 34"><path d="M10 5a4 4 0 0 1 8 0V20a7 7 0 1 1-8 0Z" fill="none" stroke="#fff" stroke-width="2.4"/><circle cx="14" cy="25" r="3.5" fill="#fff"/><path d="M22 8H30M22 13H28" stroke="#fff" stroke-width="2.4" stroke-linecap="round"/></svg>Heating</div>
  <div class="mode-btn" style="left:1260px"><svg viewBox="0 0 34 34"><path d="M4 12H22a4 4 0 1 0-4-4M4 18H28a4 4 0 1 1-4 4M4 24H16" fill="none" stroke="#fff" stroke-width="2.4" stroke-linecap="round"/></svg>Airwave</div>
  <div class="abs humidity"><svg width="18" height="22" viewBox="0 0 10 12"><path d="M5 1 C3 4 1 6 1 8 a4 4 0 0 0 8 0 C9 6 7 4 5 1Z" fill="#fff"/></svg><span>25<small>%</small></span></div>

  <section class="abs card" style="left:32px;top:428px;width:250px;height:515px"></section>
  <div class="card-title" style="left:47px;top:445px">Audio</div>
  <svg class="power" style="left:243px;top:442px" viewBox="0 0 26 26"><circle cx="13" cy="13" r="13" fill="var(--accent)"/><path d="M8.5 9 a6.5 6.5 0 1 0 9 0 M13 6 V13" fill="none" stroke="#fff" stroke-width="2" stroke-linecap="round"/></svg>
  <div class="abs album" role="img" aria-label="Album artwork, dim purple wall">
    <div class="album-meta"><div class="title">Music Title</div><div class="artist">Artist name</div></div>
    <div class="album-progress"></div>
    <svg class="album-controls" viewBox="0 0 160 26"><path d="M22 5V21M36 5L24 13L36 21Z" fill="#fff" stroke="#fff" stroke-width="2"/><circle cx="80" cy="13" r="12" fill="#fff"/><path d="M76 7L87 13L76 19Z" fill="#3a1650"/><path d="M124 5L136 13L124 21ZM138 5V21" fill="#fff" stroke="#fff" stroke-width="2"/></svg>
  </div>
  <div class="abs volume-knob"><div class="inner">50<small>%</small></div></div>
  <svg class="abs eq" viewBox="0 0 90 118"><g fill="none" stroke="var(--track)" stroke-width="7" stroke-linecap="round"><path d="M10 4V94M40 4V94M67 4V94"/></g><g fill="none" stroke="var(--track-fill)" stroke-width="7" stroke-linecap="round"><path d="M10 44V94M40 64V94M67 52V94"/></g><g fill="var(--track-fill)"><rect x="2" y="40" width="16" height="6" rx="2"/><rect x="32" y="60" width="16" height="6" rx="2"/><rect x="59" y="48" width="16" height="6" rx="2"/></g><g font-size="12" fill="var(--muted)" font-family="Roboto, sans-serif" text-anchor="middle"><text x="10" y="114">High</text><text x="40" y="114">Mid</text><text x="69" y="114">Low</text></g></svg>
  <div class="picker" style="left:122px;top:821px"><svg viewBox="0 0 14 10"><path d="M2 8 L7 3 L12 8" fill="none" stroke="currentColor" stroke-width="1.6"/></svg><span class="pk-side">Live</span><span class="pk-cur">Metal Rock</span><span class="pk-side">Rock</span><svg viewBox="0 0 14 10"><path d="M2 2 L7 7 L12 2" fill="none" stroke="currentColor" stroke-width="1.6"/></svg></div>

  <section class="abs card" style="left:297px;top:428px;width:250px;height:515px"></section>
  <div class="card-title" style="left:309px;top:443px">CCTV</div>
  <svg class="power" style="left:510px;top:440px" viewBox="0 0 26 26"><circle cx="13" cy="13" r="13" fill="var(--accent)"/><path d="M8.5 9 a6.5 6.5 0 1 0 9 0 M13 6 V13" fill="none" stroke="#fff" stroke-width="2" stroke-linecap="round"/></svg>
  <div class="cam" style="top:493px" role="img" aria-label="Camera 1 live feed, street with brick houses"><span class="cam-label">CAM 1</span><div class="cam-bar"><svg width="200" height="30" viewBox="0 0 200 30"><path d="M54 9L45 15L54 21ZM45 9L36 15L45 21Z" fill="#fff"/><circle cx="100" cy="15" r="9" fill="#fff"/><path d="M97 10L105 15L97 20Z" fill="#555"/><path d="M146 9L155 15L146 21ZM155 9L164 15L155 21Z" fill="#fff"/></svg></div></div>
  <div class="cam" style="top:721px" role="img" aria-label="Camera 2 live feed, street with brick houses"><span class="cam-label">CAM 2</span><div class="cam-bar"><svg width="200" height="30" viewBox="0 0 200 30"><path d="M54 9L45 15L54 21ZM45 9L36 15L45 21Z" fill="#fff"/><circle cx="100" cy="15" r="9" fill="#fff"/><path d="M97 10L105 15L97 20Z" fill="#555"/><path d="M146 9L155 15L146 21ZM155 9L164 15L155 21Z" fill="#fff"/></svg></div></div>

  <section class="abs card" style="left:562px;top:428px;width:515px;height:515px"></section>
  <div class="card-title" style="left:580px;top:444px">Smart TV</div>
  <svg class="power" style="left:1038px;top:442px" viewBox="0 0 26 26"><circle cx="13" cy="13" r="13" fill="var(--accent)"/><path d="M8.5 9 a6.5 6.5 0 1 0 9 0 M13 6 V13" fill="none" stroke="#fff" stroke-width="2" stroke-linecap="round"/></svg>
  <div class="abs tv-screen" role="img" aria-label="TV home screen with featured shows, top picks and app list">
    <div class="tv-hero-a"></div><div class="tv-hero-b"></div>
    <div class="tv-row"><span style="width:104px;background:linear-gradient(180deg,#f3a33c,#b9451c)"></span><span style="width:46px;background:linear-gradient(180deg,#d9d3c7,#8a9a8f)"></span><span style="width:100px;background:linear-gradient(180deg,#9fc3d8,#e3ecf0)"></span><span style="width:48px;background:linear-gradient(180deg,#3b2f8c,#7b5bd0)"></span><span style="width:66px;background:linear-gradient(180deg,#d7d2ee,#8b7fc7)"></span></div>
    <div class="tv-apps"><span></span><span></span><span></span><span></span><span></span><span></span><span></span><span></span><span></span><span></span></div>
  </div>
  <svg class="abs tv-volume" viewBox="0 0 20 297"><rect x="1" y="1" width="18" height="295" rx="9" fill="none" stroke="var(--track)" stroke-width="1.5"/><rect x="1" y="120" width="18" height="176" rx="9" fill="var(--track-fill)"/><circle cx="10" cy="120" r="7" fill="#ddd"/></svg>
  <div class="app-btn" style="left:593px;top:808px">Flixora</div>
  <div class="app-btn" style="left:708px;top:808px">Streamly</div>
  <div class="app-btn" style="left:820px;top:808px">Dreamvale+</div>
  <div class="app-btn" style="left:710px;top:876px;font-size:15px">Nimbus Video</div>
  <div class="picker" style="left:912px;top:815px"><svg viewBox="0 0 14 10"><path d="M2 8 L7 3 L12 8" fill="none" stroke="currentColor" stroke-width="1.6"/></svg><span class="pk-side">Bedroom</span><span class="pk-cur">Living Room</span><span class="pk-side">Guest Room</span><svg viewBox="0 0 14 10"><path d="M2 2 L7 7 L12 2" fill="none" stroke="currentColor" stroke-width="1.6"/></svg></div>

  <div class="abs date">05/09/2024, Friday</div>
  <svg class="abs mode-toggle" viewBox="0 0 66 22"><rect x="1" y="1" width="64" height="20" rx="10" fill="var(--toggle-bg)"/><circle cx="14" cy="11" r="9" fill="var(--toggle-knob)"/></svg>
</div>
</div>

</body>
</html>
```